High Tech Software Startup needs Letterhead Design

We need a letterhead for a startup company base in Brazil. The letterhead should combine with our logo attached here.
We are a team of professionals in Java for web and mobile with iOS and android development.
We are looking for a modern and futuristc design.

Target Market(s)

CIO, IT managers of mid to big size companies

Industry/Entity Type

It Company

```html
<!DOCTYPE html>
<html lang="pt-BR">
<head>
<meta charset="utf-8">
<title>Veltra — Letterhead options</title>
<link href="https://fonts.googleapis.com/css2?family=Inter:wght@300&family=Open+Sans:wght@600;700;800&display=swap" rel="stylesheet">
<style>
  :root {
    --board: #1d1d1d;
    --paper: #ffffff;
    --shape-light: #f4f4f4;
    --shape-dark: #e6e6e6;
    --ink-muted: #8c8c8c;
    --brand: #1f2f4a;
    --label: #f2f2f2;
  }
  * { margin: 0; padding: 0; box-sizing: border-box; }
  html, body { width: 1200px; height: 887px; overflow: hidden; background: var(--board); }
  .board { position: relative; width: 1200px; height: 887px; }

  .option-label {
    position: absolute; top: 166px; width: 380px; text-align: right;
    font-family: "Inter", sans-serif; font-weight: 300; font-size: 19px; color: var(--label);
  }
  .option-label--one { left: 195px; }
  .option-label--two { left: 657px; }

  .sheet {
    position: absolute; width: 380px; height: 491px;
    background: var(--paper); overflow: hidden;
    font-family: "Open Sans", sans-serif; color: var(--ink-muted);
  }
  .sheet--one { left: 195px; top: 195px; }
  .sheet--two { left: 657px; top: 192px; }

  .accent {
    position: absolute;
    background: linear-gradient(135deg, var(--shape-light) 0%, var(--shape-light) 35%, var(--shape-dark) 100%);
  }
  .accent--large { left: 183px; top: 0; width: 172px; height: 149px; border-radius: 0 0 26px 0; }
  .accent--medium { width: 97px; height: 97px; border-radius: 12px 0 12px 0; }
  .accent--small { width: 75px; height: 76px; border-radius: 10px 0 10px 0; }

  .sheet--one .accent--medium { left: 76px; top: 213px; }
  .sheet--one .accent--small { left: 260px; top: 370px; }
  .sheet--two .accent--medium { left: 75px; top: 191px; }
  .sheet--two .accent--small { left: 260px; top: 296px; }

  .brand {
    display: flex; align-items: center; gap: 4px;
    font-family: "Open Sans", sans-serif; font-weight: 800; color: var(--brand);
    letter-spacing: 0.3px;
  }
  .brand-square { width: 12px; height: 12px; background: var(--brand); }

  .sender-block { position: absolute; left: 17px; top: 398px; }
  .sender-block .brand { font-size: 14px; margin-bottom: 4px; }
  .sender-block .brand-square { width: 13px; height: 13px; }
  .address-lines { font-size: 5.3px; font-weight: 700; line-height: 7.1px; }
  .web-address { font-size: 7px; font-weight: 700; margin-top: 1px; }

  .footer { position: absolute; left: 8px; right: 12px; top: 468px; display: flex; align-items: flex-start; }
  .footer-col { font-size: 5.3px; font-weight: 700; line-height: 7.5px; }
  .footer-col--contact { margin-left: 12px; }
  .footer-brand { margin-left: auto; margin-top: -6px; text-align: right; }
  .footer-brand .brand { font-size: 14px; }
  .footer-brand .web-address { font-size: 5.3px; margin-top: -2px; }
</style>
</head>
<body>
<main class="board">
  <p class="option-label option-label--one">opc. 1</p>
  <p class="option-label option-label--two">opc. 2</p>

  <section class="sheet sheet--one" aria-label="Letterhead option 1">
    <div class="accent accent--large" role="img" aria-label="Faint brand decoration"></div>
    <div class="accent accent--medium" role="img" aria-label="Faint brand decoration"></div>
    <div class="accent accent--small" role="img" aria-label="Faint brand decoration"></div>
    <div class="sender-block">
      <div class="brand"><span class="brand-square"></span>VELTRA</div>
      <p class="address-lines">
        Rua das Acácias, 410 8º .<br>
        Andar Conj. 802Caixa<br>
        Postal 221 Jardim Norte<br>
        CEP 04.520-130<br>
        São Paulo - SP - Brasil<br>
        Phone: (11) 5555-0142<br>
        contato@veltra.com.br
      </p>
      <p class="web-address">www.veltra.com.br</p>
    </div>
  </section>

  <section class="sheet sheet--two" aria-label="Letterhead option 2">
    <div class="accent accent--large" role="img" aria-label="Faint brand decoration"></div>
    <div class="accent accent--medium" role="img" aria-label="Faint brand decoration"></div>
    <div class="accent accent--small" role="img" aria-label="Faint brand decoration"></div>
    <div class="footer">
      <p class="footer-col">
        Rua das Acácias, 410 8º . Andar Conj. 802Caixa<br>
        Postal 221 Jardim Norte CEP 04.520-130 São Paulo - SP - Brasil
      </p>
      <p class="footer-col footer-col--contact">
        Phone: (11) 5555-0142<br>
        contato@veltra.com.br
      </p>
      <div class="footer-brand">
        <div class="brand"><span class="brand-square"></span>VELTRA</div>
        <p class="web-address">www.veltra.com.br</p>
      </div>
    </div>
  </section>
</main>
</body>
</html>
```